PLUMBING POSTCARD DESIGN (MARKETING)

We are a local Plumbing business , Needing a post card to market domestic plumbing maintenance in my local area. The post card will have a magnet business card attached so allowance in design will need to be made. I have a slogan i want Incorporated into the design and is "TRY THE BEST, FLUSH THE REST"
I have attached my company name and logo to also incorporate into the design.
post card size 21cm L x 10cm H
business magnet card that will be attached to post card is 9cm L X 5.5cm H.
Post card will be one sided and will need following text inserted into design:
Pipewell would like to offer its fellow locals $40 off their next plumbing job. We pride ourselves in supplying the highest level of workmanship at the most competitive prices. CALL US TODAY
0431 582 907
Target Market(s)
Property owners (domestic market0
Industry/Entity Type
Plumbing
Requirements
Must have
- Eye catching, Slogan, company name and logo

```html
<!DOCTYPE html>
<html lang="en">
<head>
<meta charset="utf-8">
<title>Pipewell Postcard</title>
<link href="https://fonts.googleapis.com/css2?family=Arimo:wght@400;700&family=Raleway:wght@400;700;800&family=Roboto+Condensed:wght@700&display=swap" rel="stylesheet">
<style>
  :root{
    --blue:#1d9bd0;
    --blue-deep:#1784b8;
    --orange:#f27a24;
    --orange-light:#f6a531;
    --ink:#3a3a3a;
    --white:#ffffff;
    --page:#ebe8e4;
    --photo-a:#d8dde2;
    --photo-b:#f3f4f6;
    --photo-c:#9fb3c4;
  }
  *{box-sizing:border-box;margin:0;padding:0}
  html,body{width:1200px;height:1200px;overflow:hidden;background:var(--page)}
  .canvas{position:relative;width:1200px;height:1200px}
  .postcard{
    position:absolute;left:40px;top:333px;width:1300px;height:618px;
    transform:scale(.8615);transform-origin:top left;
    background:var(--white);overflow:hidden;
    font-family:"Arimo",Arial,sans-serif;
  }
  .abs{position:absolute}
  .side-rule{left:0;top:0;width:10px;height:500px;background:var(--blue)}
  .photo{left:470px;top:0;width:830px;height:618px;
    background:linear-gradient(100deg,var(--photo-b) 0%,var(--photo-a) 45%,var(--photo-b) 70%,var(--photo-c) 100%)}
  .shapes{left:0;top:0}
  .brand{display:flex;align-items:center;gap:12px}
  .brand-dot{width:56px;height:56px;border-radius:50%;background:var(--blue);flex:none}
  .brand-name{font-family:"Raleway",sans-serif;font-weight:800;color:var(--ink);letter-spacing:1px;line-height:1}
  .brand-sub{font-family:"Raleway",sans-serif;font-weight:400;color:var(--ink);line-height:1}
  .brand-main{left:45px;top:66px}
  .brand-main .brand-name{font-size:46px}
  .brand-main .brand-sub{font-size:22px;margin-top:8px}
  .slogan{left:42px;top:190px;line-height:70px;font-size:76px}
  .slogan span{display:block}
  .slogan .light{font-weight:400;color:var(--ink)}
  .slogan .blue{font-weight:700;color:var(--blue-deep)}
  .slogan .orange{font-weight:700;color:var(--orange)}
  .call{left:45px;top:508px;color:var(--white)}
  .call-label{font-size:30px;font-family:"Raleway",sans-serif;font-weight:400}
  .phone{font-family:"Roboto Condensed",sans-serif;font-weight:700;line-height:1}
  .call .phone{font-size:64px;margin-top:4px}
  .badge{border-radius:50%;background:var(--blue);color:var(--white);text-align:center;
    display:flex;flex-direction:column;align-items:center;justify-content:center;
    box-shadow:0 0 0 6px rgba(255,255,255,.55)}
  .badge-main{left:726px;top:26px;width:184px;height:184px}
  .badge-amount{font-weight:700;line-height:1}
  .badge-main .badge-amount{font-size:72px;margin-top:-6px}
  .badge-main .badge-note{font-size:15px;font-weight:700;line-height:18px;margin-top:6px}
  .magnet{left:703px;top:258px;width:557px;height:338px;background:var(--white);
    border-radius:18px;overflow:hidden;box-shadow:0 2px 8px rgba(0,0,0,.18)}
  .magnet-shapes{left:0;top:0}
  .brand-magnet{right:35px;top:48px}
  .brand-magnet .brand-dot{width:44px;height:44px}
  .brand-magnet .brand-name{font-size:36px}
  .brand-magnet .brand-sub{font-size:17px;margin-top:6px}
  .magnet-call{right:35px;top:180px;text-align:right}
  .magnet-call .call-label{color:var(--ink);font-size:24px}
  .magnet-call .phone{color:var(--blue-deep);font-size:52px;margin-top:4px}
  .badge-magnet{left:24px;top:120px;width:130px;height:130px;box-shadow:0 0 0 5px rgba(255,255,255,.6)}
  .badge-magnet .badge-amount{font-size:54px}
  .badge-magnet .badge-note{font-size:24px;font-weight:700;line-height:1}
  .offer{left:27px;top:274px;color:var(--white)}
  .offer-title{font-size:16px;font-weight:700;white-space:nowrap}
  .offer-copy{font-size:12px;line-height:16px;margin-top:4px;white-space:nowrap}
</style>
</head>
<body>
<div class="canvas">
  <div class="postcard">
    <div class="abs photo" role="img" aria-label="Photo of a smiling plumber with tool belt standing beside a white work van"></div>

    <svg class="abs shapes" width="1300" height="618" viewBox="0 0 1300 618">
      <defs>
        <linearGradient id="bandOrange" x1="0" y1="0" x2="0" y2="1">
          <stop offset="0" stop-color="var(--orange-light)"/>
          <stop offset="1" stop-color="var(--orange)"/>
        </linearGradient>
      </defs>
      <polygon points="685,0 1000,0 760,150" fill="url(#bandOrange)"/>
      <polygon points="1000,0 1300,0 1300,125 880,125" fill="var(--blue)"/>
      <polygon points="0,496 370,496 510,618 0,618" fill="url(#bandOrange)"/>
      <polygon points="380,496 400,496 540,618 520,618" fill="var(--white)"/>
      <polygon points="408,496 428,496 568,618 548,618" fill="var(--white)"/>
      <polygon points="420,540 440,540 530,618 510,618" fill="var(--orange)"/>
    </svg>

    <div class="abs side-rule"></div>

    <div class="abs brand brand-main">
      <div class="brand-dot"></div>
      <div>
        <div class="brand-name">PIPEWELL</div>
        <div class="brand-sub">PLUMBING | DRAINAGE | GAS</div>
      </div>
    </div>

    <h1 class="abs slogan">
      <span class="light">TRY</span>
      <span class="blue">THE BEST</span>
      <span class="light">FLUSH</span>
      <span class="orange">THE REST</span>
    </h1>

    <div class="abs call">
      <div class="call-label">CALL US TODAY</div>
      <div class="phone">0431-582-907</div>
    </div>

    <div class="abs badge badge-main">
      <div class="badge-amount">$40</div>
      <div class="badge-note">OFF THEIR<br>NEXT PLUMBING<br>JOB</div>
    </div>

    <div class="abs magnet">
      <svg class="abs magnet-shapes" width="557" height="338" viewBox="0 0 557 338">
        <polygon points="0,130 440,338 0,338" fill="url(#bandOrange)"/>
        <polygon points="440,338 557,268 557,338" fill="var(--blue)"/>
      </svg>

      <div class="abs brand brand-magnet">
        <div class="brand-dot"></div>
        <div>
          <div class="brand-name">PIPEWELL</div>
          <div class="brand-sub">PLUMBING | DRAINAGE | GAS</div>
        </div>
      </div>

      <div class="abs magnet-call">
        <div class="call-label">CALL US TODAY</div>
        <div class="phone">0431-582-907</div>
      </div>

      <div class="abs badge badge-magnet">
        <div class="badge-amount">$40</div>
        <div class="badge-note">OFF</div>
      </div>

      <div class="abs offer">
        <div class="offer-title">THEIR NEXT PLUMBING JOB</div>
        <div class="offer-copy">We pride ourselves in supplying the highest<br>level of workmanship at the most competitive prices.</div>
      </div>
    </div>
  </div>
</div>
</body>
</html>
```